menu buttom design

We are looking for a menu button design, similar too the one we have posted in the files section.
They must be quite big and prominent on the page. They will be down the right hand side of the website which has a large video player on as well. We would like them to look a little like TV buttons, not not cliched.
The titles on each button are as follows:
Whats new, Buy and sell, Join in, More TV, More Info, more web
The web page will be black.
PLEASE concentrate more on the colours and text that making the buttons different shapes.
It must look classy, sophistocated, beautiful design

Target Market(s)

Web Tv watchers

Requirements
Must have
• Should be similar to what I have uploaded on the file.
Should be rectangular, raised up to give button effect with some shine.
What we would really like to to have some sorts of graphics behind the text to show the various
pages. We would like more subtle, maybe pastel colours that work well together and a really nice font that works well.
Concentrate more on the colours and fonts and the overall look rather than different shapes.
These buttons are for mock up web pages, but when the pages are made we will us the buttons as templates and will animate them when you roll over them.

```html
<!DOCTYPE html>
<html lang="en">
<head>
<meta charset="utf-8">
<title>Menu Buttons</title>
<link rel="stylesheet" href="https://fonts.googleapis.com/css2?family=Didact+Gothic&display=swap">
<style>
  :root {
    --page-bg: #000000;
    --label: #ffffff;

    --frame-light-top: #f2f2f2;
    --frame-light-bottom: #9c9c9c;
    --frame-dark-top: #5a5a5a;
    --frame-dark-bottom: #262626;

    --red-top: #f2505c;
    --red-mid: #dc0f1c;
    --red-bottom: #b8000a;

    --yellow-top: #ffe264;
    --yellow-mid: #ffc60a;
    --yellow-bottom: #f4a800;

    --blue-top: #5cc4ef;
    --blue-mid: #1591d0;
    --blue-bottom: #0a6aa6;

    --orange-top: #ff9a52;
    --orange-mid: #ff6a10;
    --orange-bottom: #e85000;

    --green-top: #5fe04c;
    --green-mid: #1fbe12;
    --green-bottom: #0e9a04;

    --purple-top: #dc7cec;
    --purple-mid: #a82cc8;
    --purple-bottom: #7c0a9c;
  }

  * { box-sizing: border-box; margin: 0; padding: 0; }

  html, body {
    width: 1200px;
    height: 900px;
    overflow: hidden;
    background: var(--page-bg);
  }

  .canvas {
    position: relative;
    width: 1200px;
    height: 900px;
    background: var(--page-bg);
    font-family: "Didact Gothic", "Century Gothic", sans-serif;
  }

  .button-set {
    position: absolute;
    top: 55px;
    display: grid;
    grid-template-columns: repeat(2, 262px);
    grid-template-rows: repeat(3, 210px);
    column-gap: 20px;
    row-gap: 79px;
  }

  .button-set--light { left: 22px; }
  .button-set--dark { left: 631px; }

  .menu-button {
    position: relative;
    border-radius: 9px;
    padding: 6px;
  }

  .button-set--light .menu-button {
    background: linear-gradient(180deg, var(--frame-light-top), var(--frame-light-bottom));
    box-shadow: inset 0 0 0 1px rgba(255,255,255,0.6);
  }

  .button-set--dark .menu-button {
    background: linear-gradient(180deg, var(--frame-dark-top), var(--frame-dark-bottom));
    box-shadow: inset 0 0 0 1px rgba(255,255,255,0.15);
  }

  .menu-button__face {
    position: relative;
    width: 100%;
    height: 100%;
    border-radius: 10px;
    overflow: hidden;
    display: flex;
    align-items: center;
    justify-content: center;
    text-align: center;
    box-shadow:
      inset 0 0 0 2px rgba(255,255,255,0.35),
      inset 0 -6px 10px rgba(0,0,0,0.18);
  }

  .menu-button__face::before {
    content: "";
    position: absolute;
    left: 0; right: 0; top: 0;
    height: 48%;
    background: linear-gradient(180deg, rgba(255,255,255,0.38), rgba(255,255,255,0.08));
    border-radius: 10px 10px 60% 60% / 10px 10px 14px 14px;
  }

  .menu-button__label {
    position: relative;
    color: var(--label);
    font-size: 47px;
    line-height: 1.18;
    letter-spacing: 0.5px;
    text-transform: uppercase;
    text-shadow: 0 1px 2px rgba(0,0,0,0.2);
  }

  .menu-button__label small {
    display: block;
    font-size: 32px;
    line-height: 1.05;
  }

  .menu-button--red .menu-button__face {
    background: linear-gradient(180deg, var(--red-top) 0%, var(--red-mid) 50%, var(--red-bottom) 100%);
  }
  .menu-button--yellow .menu-button__face {
    background: linear-gradient(180deg, var(--yellow-top) 0%, var(--yellow-mid) 50%, var(--yellow-bottom) 100%);
  }
  .menu-button--blue .menu-button__face {
    background: linear-gradient(180deg, var(--blue-top) 0%, var(--blue-mid) 50%, var(--blue-bottom) 100%);
  }
  .menu-button--orange .menu-button__face {
    background: linear-gradient(180deg, var(--orange-top) 0%, var(--orange-mid) 50%, var(--orange-bottom) 100%);
  }
  .menu-button--green .menu-button__face {
    background: linear-gradient(180deg, var(--green-top) 0%, var(--green-mid) 50%, var(--green-bottom) 100%);
  }
  .menu-button--purple .menu-button__face {
    background: linear-gradient(180deg, var(--purple-top) 0%, var(--purple-mid) 50%, var(--purple-bottom) 100%);
  }
</style>
</head>
<body>
<main class="canvas">

  <nav class="button-set button-set--light" aria-label="Menu buttons, silver frame">
    <div class="menu-button menu-button--red"><div class="menu-button__face"><span class="menu-button__label">Whats<br>New</span></div></div>
    <div class="menu-button menu-button--yellow"><div class="menu-button__face"><span class="menu-button__label">More<br>TV</span></div></div>
    <div class="menu-button menu-button--blue"><div class="menu-button__face"><span class="menu-button__label">Buy<small>and</small>Sell</span></div></div>
    <div class="menu-button menu-button--orange"><div class="menu-button__face"><span class="menu-button__label">More<br>Info</span></div></div>
    <div class="menu-button menu-button--green"><div class="menu-button__face"><span class="menu-button__label">Join<br>In</span></div></div>
    <div class="menu-button menu-button--purple"><div class="menu-button__face"><span class="menu-button__label">More<br>Web</span></div></div>
  </nav>

  <nav class="button-set button-set--dark" aria-label="Menu buttons, graphite frame">
    <div class="menu-button menu-button--red"><div class="menu-button__face"><span class="menu-button__label">Whats<br>New</span></div></div>
    <div class="menu-button menu-button--yellow"><div class="menu-button__face"><span class="menu-button__label">More<br>TV</span></div></div>
    <div class="menu-button menu-button--blue"><div class="menu-button__face"><span class="menu-button__label">Buy<small>and</small>Sell</span></div></div>
    <div class="menu-button menu-button--orange"><div class="menu-button__face"><span class="menu-button__label">More<br>Info</span></div></div>
    <div class="menu-button menu-button--green"><div class="menu-button__face"><span class="menu-button__label">Join<br>In</span></div></div>
    <div class="menu-button menu-button--purple"><div class="menu-button__face"><span class="menu-button__label">More<br>Web</span></div></div>
  </nav>

</main>
</body>
</html>
```